The task involves the design and creation of a wordpress website for plainpactly.co.
Plainpactly.co is a website through which people can purchase template legal contracts.The website is focused on Australian users although in the future we may target users in other countries.
*************************************************
We will offer 3 bundles of products (a small business, medium business and a large business bundle) as follows:
(a) a Starter package ($199);
(b) a Pro (professional) package ($499);
(c) an Enterprise package ($1,500).
Each bundle contains a number of legal templates. The Pro package includes all of the legal templates in the Starter package. The Enterprise version contains all the legal templates in the Starter and Pro package.
The starter bundle will include the following legal documents:
+Website terms and conditions
+Confidentiality agreement
+Services agreement
+Purchase order terms and conditions
+Variation agreement
+Independent contractor agreement
+Term sheet
The Pro bundle includes:
+ all of the documents contained in the Starter package plus
+ Request for tender
+ Consultancy agreement
+ Contract labour agreement
+ Sponsorship agreement
The Enterprise package includes:
+All of the documents in our Pro package plus
+Freight Services agreement
+IT Services agreement
+Website design and hosting agreement
+Teaming agreement
+Long form services agreement
+Distribution agreement
+Content supply agreement
****************************************************
We like the simplicity and layout of the following websites:
http://leavewatchr.com/
https://www.trygleanly.com/
http://www.fornavo.com/
http://www.quillrule.com/
http://usebrimo.com/
We like the way on the leavewatchr.com page when you click on the pricing tab and other tabs of the navigation bar you are taken lower down on the homepage to the content. We like the static header on leavewatchr and Fornavo. We also like the use of big headings, images and symbols to convey meaning as well as having the webpage broken into sections.
We will want an email sign up capability and will need to integrate an email collection capability with postwren or similar.
We like the way it is referred to on the https://www.ledgerpleader.com/ website where it says:
"Your first document is free" and them there is an email sign up box.
We imagine having a similar features at a couple of places on the site with a call to action.
We also imagine including some sort of website abandonment application similar to http://leavewatchr.com/ or http://stayhold.com/. We would also like a countdown clock linked to a discount off the price of the bundles. Please provide a recommendation and ensure that this can easily be integrated.
We will need an e-commence capability so that we can sell our products.
******************************************
Our value proposition is as follows:
1. Lower your legal costs by using our template documents as a starting point
Why pay a lawyer to create a document from scratch when you can you our template agreements as the starting point.
2. Variety of bundles to chose from
We offer you the opportunity to purchase the bundle of documents that are just right for you – small business, medium business and large business options.
3.Customise agreements yourself or have your lawyer customise them for you.
Our contracts are drafted in plain English and you can provide them to your lawyer and ask them to customise them for you.
4. Reviewed by top lawyers - customised for Australia
All of our legal documents have been reviewed by a lawyer with experience working at a top international law firm.
***************************************************
The benefits of the service are:
* Documents reviewed by Australian lawyer with experience at top tier Australian law firm.
* Cost effective approach to risk management
* Electronic delivery
* Use templates as often as you like for your internal business purposes
* Free explanation of each template agreement
* Sensible approach to legal drafting to minimise contract negotiation time
*****************************************************
We will need to include the following across the bottom of each webpage.
"Copyright 2014 PlainPactly. All rights reserved. PlainPactly provides information only. PlainPactly is not a "lawyer referral service" and does not provide legal advice or participate in any legal representation. PlainPactly is not a law firm or a substitute for a qualified lawyer or law firm. For legal advice, please contact a lawyer. Use of PlainPactly.co is subject to our Terms and Conditions."
The reference to Terms and Conditions will be a link to the Terms and Conditions.
*********************************************************
The Contact Us section should be a simple webform. We will not include any telephone or physical address at this stage.
For the About Us section
We can include the following:
PlainPactly was conceived and nurtured in Melbourne, the world's most liveable city by an experienced lawyer who loves the idea of making legal contracting affordable for small and medium size businesses. We have friends in other cities who help make PlainPactly possible.
************************************************************
We expect the website created to be user friendly, able to be updated easily, optimised for search engines and to be built on wordpress. The website should be able to integrate with third party applications (eg analytic software, email marketing tools etc). Please include recommendations for third party software for integration. We have installed Wordpress 3.9.
Target Market(s)
Small to medium business owners.

```html
<!DOCTYPE html>
<html lang="en">
<head>
<meta charset="utf-8">
<title>PlainPactly.co – Template Legal Contracts</title>
<link rel="stylesheet" href="https://fonts.googleapis.com/css2?family=Zilla+Slab:wght@400;500&family=Arimo&display=swap">
<style>
  :root {
    --teal: #06b5c5;
    --teal-dark: #0aa3b2;
    --white: #ffffff;
    --ink: #2b2b2b;
    --muted: #7a7a7a;
    --page: #f3f3f3;
    --line: #dddddd;
    --price: #4f8f2f;
    --hero-dark: #1b1b1e;
  }
  * { box-sizing: border-box; margin: 0; padding: 0; }
  html, body { width: 1200px; height: 1000px; overflow: hidden; }
  body {
    position: relative;
    background: var(--page);
    font-family: "Zilla Slab", Georgia, serif;
    color: var(--ink);
  }
  a { color: inherit; text-decoration: none; }

  .topbar {
    position: absolute; left: 0; top: 0; width: 1200px; height: 35px;
    background: var(--teal); color: var(--white);
    box-shadow: 0 2px 4px rgba(0,0,0,.2); z-index: 2;
    font-size: 13px;
  }
  .cart { position: absolute; left: 176px; top: 9px; display: flex; align-items: center; gap: 6px; }
  .account-links { position: absolute; right: 203px; top: 10px; display: flex; gap: 17px; }

  .masthead {
    position: absolute; left: 0; top: 35px; width: 1200px; height: 64px;
    background: var(--white); border-bottom: 1px solid var(--line);
  }
  .brand {
    position: absolute; left: 176px; top: 18px;
    font-size: 25px; font-weight: 500; color: var(--teal);
  }
  .main-nav { position: absolute; left: 655px; top: 21px; display: flex; gap: 25px; font-size: 13px; }
  .main-nav .current { color: var(--teal); }

  .hero {
    position: absolute; left: 0; top: 99px; width: 1200px; height: 400px;
    background:
      linear-gradient(90deg, rgba(214,170,80,.85) 0%, rgba(120,80,40,.7) 25%, rgba(30,25,22,.9) 45%, rgba(60,65,75,.9) 65%, rgba(210,205,195,.85) 85%, rgba(70,70,75,.9) 100%),
      var(--hero-dark);
  }
  .hero-title {
    position: absolute; left: 176px; top: 107px; height: 50px;
    padding: 0 11px; background: rgba(30,30,30,.65);
    color: var(--white); font-size: 28px; font-weight: 500; line-height: 50px;
  }
  .hero-lede {
    position: absolute; left: 176px; top: 176px; width: 784px; height: 38px;
    padding: 0 18px; background: rgba(40,40,40,.65);
    color: var(--white); font-size: 15.5px; line-height: 38px;
  }
  .hero-cta {
    position: absolute; left: 176px; top: 228px; width: 222px; height: 43px;
    background: var(--teal); border-radius: 3px; color: var(--white);
    font-size: 20px; font-weight: 500; text-align: center; line-height: 43px;
  }
  .slider-dots { position: absolute; left: 563px; top: 368px; display: flex; gap: 8px; }
  .slider-dots span { width: 14px; height: 14px; border-radius: 50%; background: #888; border: 2px solid #888; }
  .slider-dots .active { background: #ccc; }

  .section-rule { position: absolute; left: 0; top: 503px; width: 1200px; border-top: 1px solid var(--line); }

  .section-tab {
    position: absolute; left: 176px; top: 541px; width: 163px; height: 44px;
    border: 1px solid var(--line); background: #f1f1f1;
    font-size: 14px; color: #555; text-align: center; line-height: 42px;
  }

  .product-grid { position: absolute; left: 176px; top: 620px; display: flex; gap: 19px; }
  .product-card {
    width: 196px; height: 288px; background: var(--white);
    box-shadow: 0 1px 3px rgba(0,0,0,.25); padding: 8px;
  }
  .product-tile {
    height: 132px; background: var(--teal); color: var(--white);
    font-family: "Arimo", Arial, sans-serif; font-size: 33px; line-height: 39px;
    display: flex; align-items: center; justify-content: center; text-align: center;
  }
  .product-price { margin-top: 16px; font-size: 16px; color: var(--price); }
  .product-name { margin-top: 5px; font-size: 14.5px; }
  .product-summary { margin-top: 6px; font-size: 11px; line-height: 16px; color: var(--muted); }

  .more-link { position: absolute; right: 190px; top: 947px; font-size: 13px; color: #666; }
  .more-link a { color: var(--teal); letter-spacing: .5px; }
  .footer-rule { position: absolute; left: 0; top: 992px; width: 1200px; border-top: 1px solid var(--line); }
</style>
</head>
<body>
  <div class="topbar">
    <div class="cart">
      <svg width="18" height="14" viewBox="0 0 18 14" fill="none" stroke="#fff" stroke-width="1.4">
        <path d="M1 1h3l2 8h9l2-6H5"/><circle cx="7" cy="12" r="1.2"/><circle cx="14" cy="12" r="1.2"/>
      </svg>
      <span>0 items - ( $0 in total )</span>
    </div>
    <nav class="account-links"><a href="#">Register</a><a href="#">Login</a></nav>
  </div>

  <header class="masthead">
    <a class="brand" href="#">PlainPactly.co</a>
    <nav class="main-nav">
      <a class="current" href="#">Home</a><a href="#">About</a><a href="#">Products</a><a href="#">My Account</a><a href="#">Contact</a>
    </nav>
  </header>

  <section class="hero" role="img" aria-label="Photo of a lawyer in a suit signing a document in front of law book shelves">
    <h1 class="hero-title">Enterprise package</h1>
    <p class="hero-lede">Built for big business, this package combines all our offerings to meet the needs of larger organisations</p>
    <a class="hero-cta" href="#">Buy Now</a>
    <div class="slider-dots"><span></span><span class="active"></span><span></span></div>
  </section>

  <div class="section-rule"></div>
  <div class="section-tab">Document Package</div>

  <div class="product-grid">
    <article class="product-card">
      <div class="product-tile">XYZ<br>Document</div>
      <p class="product-price">Free</p>
      <h2 class="product-name">Free Doucment</h2>
      <p class="product-summary">To demonstrate our capacity to develop and deliver quality legal documentation, please accept this document …</p>
    </article>
    <article class="product-card">
      <div class="product-tile">Enterprise<br>Package</div>
      <p class="product-price">$1,500</p>
      <h2 class="product-name">Enterprise Package</h2>
      <p class="product-summary">Our Enterprise Package provides a holistic solution for large business! All of the documents contained in the Starter and …</p>
    </article>
    <article class="product-card">
      <div class="product-tile">Pro<br>Package</div>
      <p class="product-price">$499</p>
      <h2 class="product-name">Pro Package</h2>
      <p class="product-summary">Our Professional Package is targeted towards medium business’ and includes everything you need as a …</p>
    </article>
    <article class="product-card">
      <div class="product-tile">Standard<br>Package</div>
      <p class="product-price">$199</p>
      <h2 class="product-name">Standard Package</h2>
      <p class="product-summary">Our small business bundle includes everything you need to establish yourself!&nbsp; Example text will continue …</p>
    </article>
  </div>

  <p class="more-link">Document Package: <a href="#">More items</a></p>
  <div class="footer-rule"></div>
</body>
</html>
```